" PRESTA SERVIÇOS DE TECNOLOGIA (T.I.) COMO: DESENVOLVIMENTO E IMPLANTAÇAO DE SISTEMAS, ERP, HELPDESK, HOST, CLOUD... EXCLUSIVAMENTE NO SEGMENTO DE SAUDE (HOSPITAIS E CLINICAS) "

```html
<!DOCTYPE html>
<html lang="pt-BR">
<head>
<meta charset="UTF-8">
<title>Clinara Sistemas – Cartão de visita</title>
<link href="https://fonts.googleapis.com/css2?family=Arimo:wght@400&display=swap" rel="stylesheet">
<style>
  :root {
    --page-bg: #e9e7e4;
    --card-white: #ffffff;
    --card-blue: #2d5b82;
    --accent-green: #8cc63f;
    --brand-blue: #2a9fd8;
    --tagline-grey: #6b6b6b;
    --contact-white: #ffffff;
  }
  * { margin: 0; padding: 0; box-sizing: border-box; }
  html, body {
    width: 1200px; height: 1200px; overflow: hidden;
    background: var(--page-bg);
  }
  .business-card {
    position: absolute;
    left: 80px; top: 443px;
    width: 1040px; height: 314px;
    background: var(--card-white);
    box-shadow: 0 6px 18px rgba(0,0,0,0.18);
    overflow: hidden;
  }
  .card-shapes { position: absolute; inset: 0; }
  .brand {
    position: absolute;
    left: 40px; top: 126px;
    width: 340px;
    text-align: center;
    font-family: "Arimo", sans-serif;
  }
  .brand-name {
    font-size: 38px;
    font-weight: 400;
    color: var(--brand-blue);
    line-height: 1;
  }
  .brand-tagline {
    margin-top: 10px;
    font-size: 13px;
    font-weight: 400;
    color: var(--tagline-grey);
  }
  .contact {
    position: absolute;
    right: 0; top: 0;
    width: 560px; height: 100%;
    font-family: "Arimo", sans-serif;
    color: var(--contact-white);
    font-size: 13px;
  }
  .person {
    position: absolute;
    right: 80px; top: 38px;
    text-align: center;
    line-height: 1.35;
  }
  .person-name { font-size: 14px; }
  .contact-line {
    position: absolute;
    right: 80px;
    text-align: right;
    line-height: 1.35;
  }
  .line-phone { top: 122px; }
  .line-email { top: 168px; }
  .line-social { top: 200px; }
  .line-address { top: 232px; }
  .contact-icon {
    position: absolute;
    right: 34px;
    width: 22px; height: 22px;
  }
  .icon-phone { top: 124px; }
  .icon-email { top: 164px; }
  .icon-social { top: 197px; }
  .icon-pin { top: 231px; }
</style>
</head>
<body>
  <div class="business-card">
    <svg class="card-shapes" width="1040" height="314" viewBox="0 0 1040 314" aria-hidden="true">
      <polygon points="465,0 477,0 396,314 384,314" fill="var(--accent-green)"/>
      <polygon points="488,0 1040,0 1040,314 407,314" fill="var(--card-blue)"/>
    </svg>

    <div class="brand">
      <div class="brand-name">Clinara Sistemas</div>
      <div class="brand-tagline">Soluções de TI para a área da saúde</div>
    </div>

    <div class="contact">
      <div class="person">
        <div class="person-name">Nome/Sobre nome</div>
        <div class="person-role">cargo</div>
      </div>

      <div class="contact-line line-phone">55° 55-5555-5555<br>55° 55-5555-5555</div>
      <div class="contact-line line-email">clinara@exemplo.com.br</div>
      <div class="contact-line line-social">exemplo@rede.com.br</div>
      <div class="contact-line line-address">end. Rua dos Exemplos | Bairro<br>Cidade | Estado | CEP. 00000-000</div>

      <svg class="contact-icon icon-phone" viewBox="0 0 24 24" aria-hidden="true">
        <path d="M9 3 L12 8 L10 10 Q11 14 14 15 L16 13 L21 16 L19 20 Q10 21 5 11 Q4 6 9 3 Z" fill="#fff" transform="rotate(20 12 12)"/>
      </svg>
      <svg class="contact-icon icon-email" viewBox="0 0 24 24" aria-hidden="true">
        <rect x="3" y="6" width="18" height="12" fill="none" stroke="#fff" stroke-width="1.6"/>
        <path d="M3 6 L12 13 L21 6" fill="none" stroke="#fff" stroke-width="1.6"/>
      </svg>
      <svg class="contact-icon icon-social" viewBox="0 0 24 24" aria-hidden="true">
        <rect x="4" y="4" width="16" height="16" rx="2" fill="#fff"/>
      </svg>
      <svg class="contact-icon icon-pin" viewBox="0 0 24 24" aria-hidden="true">
        <path d="M12 2 C7.5 2 5 5.5 5 9 C5 14 12 22 12 22 C12 22 19 14 19 9 C19 5.5 16.5 2 12 2 Z" fill="#fff"/>
        <circle cx="12" cy="9" r="2.8" fill="var(--card-blue)"/>
      </svg>
    </div>
  </div>
</body>
</html>
```